"Got Radon?" Banner Ads

I need banner ads made for Pelvaro Banner Circuit campaign. There are 10 sizes of banners, so I need all 10 sizes. All of them can be similar in design and concept, but need to look good and the content must fill the space nicely.

The text on the ad is "Got Radon?" big/bold, and there should be a picture of a house with gas seeping into it from the ground. I have attached an example of an existing ad for reference.

These are the 10 sizes of banners that we need:
970x90
120x600
160x600
200x200
250x250
350x250
300x600
336x280
468x60
728x90

```html
<!DOCTYPE html>
<html lang="en">
<head>
<meta charset="utf-8">
<title>Got Radon? Banner Set – Pelvaro Banner Circuit</title>
<link rel="stylesheet" href="https://fonts.googleapis.com/css2?family=Montserrat:wght@700;800&display=swap">
<style>
:root{
  --sheet:#ffffff;
  --brand-yellow:#ffff00;
  --brand-ink:#1c2f6e;
  --sky-blue:#3d6fcc;
  --sky-deep:#2f5fbf;
  --band-red:#a50d0d;
  --headline:#ffffff;
  --label:#111111;
  --house-warm:#b9855a;
  --house-cool:#8e9aa6;
  --gas-green:#7fbf4f;
}
html,body{margin:0;padding:0;overflow:hidden}
body{width:1200px;height:1200px;background:var(--sheet);position:relative;font-family:"Montserrat",Arial,sans-serif}

.size-label{position:absolute;font-family:Arial,Helvetica,sans-serif;font-size:23px;color:var(--label);line-height:1}

.banner{position:absolute;overflow:hidden;background:linear-gradient(160deg,var(--sky-blue),var(--sky-deep))}
.banner > *{position:absolute}

.yellow-wedge{left:0;top:0;height:100%}
.header-band{left:0;top:0;width:100%;background:var(--brand-yellow);border-radius:0 0 50% 50% / 0 0 6px 6px}

.brand-name{color:var(--brand-ink);font-weight:700;line-height:1.1;white-space:nowrap;text-align:center}

.headline{color:var(--headline);font-weight:700;line-height:1.15;white-space:nowrap;text-shadow:0 2px 3px rgba(0,0,0,.35)}

.house-art{background:linear-gradient(135deg,#8a4a2a 0%,var(--house-warm) 35%,#d9c7a4 55%,var(--house-cool) 80%,var(--gas-green) 100%)}

.offer-band{left:0;width:100%;background:var(--band-red);color:#fff;font-weight:700;line-height:1.3;box-sizing:border-box}
.offer-band .offer-main{display:block;text-transform:uppercase;font-weight:800}

/* 970x90 */
.b970{left:96px;top:70px;width:776px;height:72px}
.b970 .brand-name{left:22px;top:25px;font-size:20px;text-align:left}
.b970 .headline{left:309px;top:14px;font-size:38px}
.b970 .house-art{left:580px;top:0;width:196px;height:72px}

/* 728x90 */
.b728{left:96px;top:179px;width:582px;height:72px}
.b728 .brand-name{left:16px;top:27px;font-size:16px;text-align:left}
.b728 .headline{left:224px;top:18px;font-size:28px}
.b728 .house-art{left:430px;top:0;width:152px;height:72px}

/* 468x60 */
.b468{left:96px;top:294px;width:374px;height:48px}
.b468 .brand-name{left:10px;top:18px;font-size:10.5px;text-align:left}
.b468 .headline{left:144px;top:12px;font-size:18px}
.b468 .house-art{left:272px;top:0;width:102px;height:48px}

/* 350x250 */
.b350{left:96px;top:395px;width:280px;height:200px}
.b350 .header-band{height:66px}
.b350 .brand-name{left:0;width:100%;top:21px;font-size:22px}
.b350 .headline{left:21px;top:84px;font-size:35px;line-height:1.25}
.b350 .house-art{left:172px;top:96px;width:108px;height:104px}

/* 336x280 */
.b336{left:409px;top:371px;width:269px;height:224px}
.b336 .header-band{height:64px}
.b336 .brand-name{left:0;width:100%;top:20px;font-size:21px}
.b336 .headline{left:0;width:100%;text-align:center;top:80px;font-size:33px}
.b336 .house-art{left:40px;top:130px;width:229px;height:94px}

/* 250x250 */
.b250{left:711px;top:395px;width:200px;height:200px}
.b250 .header-band{height:46px}
.b250 .brand-name{left:0;width:100%;top:14px;font-size:16px}
.b250 .headline{left:0;width:100%;text-align:center;top:60px;font-size:26px}
.b250 .house-art{left:6px;top:112px;width:194px;height:88px}

/* 200x200 */
.b200{left:945px;top:435px;width:160px;height:160px}
.b200 .header-band{height:37px}
.b200 .brand-name{left:0;width:100%;top:11px;font-size:13px}
.b200 .headline{left:0;width:100%;text-align:center;top:49px;font-size:21px}
.b200 .house-art{left:6px;top:94px;width:154px;height:66px}

/* 300x600 */
.b300{left:96px;top:642px;width:240px;height:480px}
.b300 .header-band{height:54px}
.b300 .brand-name{left:0;width:100%;top:16px;font-size:19px}
.b300 .headline{left:0;width:100%;text-align:center;top:80px;font-size:32px}
.b300 .house-art{left:0;top:130px;width:240px;height:238px}
.b300 .offer-band{top:368px;height:112px;padding:16px 0 0 20px;font-size:17px}
.b300 .offer-band .offer-main{font-size:18.5px}

/* 160x600 */
.b160{left:444px;top:642px;width:128px;height:480px}
.b160 .header-band{height:62px}
.b160 .brand-name{left:0;width:100%;top:12px;font-size:16px}
.b160 .headline{left:0;width:100%;text-align:center;top:86px;font-size:16px}
.b160 .house-art{left:0;top:138px;width:128px;height:252px}
.b160 .offer-band{top:390px;height:90px;padding:20px 0 0 9px;font-size:9.5px}
.b160 .offer-band .offer-main{font-size:10.5px}

/* 120x600 */
.b120{left:680px;top:642px;width:96px;height:480px}
.b120 .header-band{height:61px}
.b120 .brand-name{left:0;width:100%;top:14px;font-size:13px}
.b120 .headline{left:0;width:100%;text-align:center;top:78px;font-size:16px;line-height:1.4}
.b120 .house-art{left:0;top:146px;width:96px;height:204px}
.b120 .offer-band{top:350px;height:130px;padding:10px 0 0 9px;font-size:11.5px;line-height:1.2}
.b120 .offer-band .offer-main{font-size:12.5px}
.b120 .offer-band .offer-line{display:block;margin-top:6px}
</style>
</head>
<body>

<!-- Leaderboards -->
<div class="banner b970">
  <svg class="yellow-wedge" width="260" height="72" viewBox="0 0 260 72"><path d="M0 0H244Q252 36 188 72H0Z" fill="var(--brand-yellow)"/></svg>
  <div class="brand-name">Clearvale Radon</div>
  <div class="headline">Got Radon?</div>
  <div class="house-art" role="img" aria-label="Cutaway illustration of a house with green radon gas seeping up from the ground"></div>
</div>
<div class="size-label" style="left:894px;top:108px">970x90</div>

<div class="banner b728">
  <svg class="yellow-wedge" width="200" height="72" viewBox="0 0 200 72"><path d="M0 0H184Q192 36 136 72H0Z" fill="var(--brand-yellow)"/></svg>
  <div class="brand-name">Clearvale Radon</div>
  <div class="headline">Got Radon?</div>
  <div class="house-art" role="img" aria-label="Cutaway illustration of a house with green radon gas seeping up from the ground"></div>
</div>
<div class="size-label" style="left:701px;top:218px">728x90</div>

<div class="banner b468">
  <svg class="yellow-wedge" width="130" height="48" viewBox="0 0 130 48"><path d="M0 0H120Q126 24 84 48H0Z" fill="var(--brand-yellow)"/></svg>
  <div class="brand-name">Clearvale Radon</div>
  <div class="headline">Got Radon?</div>
  <div class="house-art" role="img" aria-label="Cutaway illustration of a house with green radon gas seeping up from the ground"></div>
</div>
<div class="size-label" style="left:485px;top:313px">468x60</div>

<!-- Rectangles and squares -->
<div class="banner b350">
  <div class="header-band"></div>
  <div class="brand-name">Clearvale Radon</div>
  <div class="headline">Got<br>Radon?</div>
  <div class="house-art" role="img" aria-label="Cutaway illustration of a house with green radon gas seeping up from the ground"></div>
</div>
<div class="size-label" style="left:98px;top:604px">350x250</div>

<div class="banner b336">
  <div class="header-band"></div>
  <div class="brand-name">Clearvale Radon</div>
  <div class="headline">Got Radon?</div>
  <div class="house-art" role="img" aria-label="Cutaway illustration of a house with green radon gas seeping up from the ground"></div>
</div>
<div class="size-label" style="left:408px;top:604px">336x280</div>

<div class="banner b250">
  <div class="header-band"></div>
  <div class="brand-name">Clearvale Radon</div>
  <div class="headline">Got Radon?</div>
  <div class="house-art" role="img" aria-label="Cutaway illustration of a house with green radon gas seeping up from the ground"></div>
</div>
<div class="size-label" style="left:708px;top:604px">250x250</div>

<div class="banner b200">
  <div class="header-band"></div>
  <div class="brand-name">Clearvale Radon</div>
  <div class="headline">Got Radon?</div>
  <div class="house-art" role="img" aria-label="Cutaway illustration of a house with green radon gas seeping up from the ground"></div>
</div>
<div class="size-label" style="left:947px;top:604px">200x200</div>

<!-- Skyscrapers -->
<div class="banner b300">
  <div class="header-band"></div>
  <div class="brand-name">Clearvale Radon</div>
  <div class="headline">Got Radon?</div>
  <div class="house-art" role="img" aria-label="Cutaway illustration of a two-storey house interior with green radon gas rising from the basement"></div>
  <div class="offer-band"><span class="offer-main">Free Estimates</span>Same Day Service<br>Best Price Guarantee</div>
</div>
<div class="size-label" style="left:98px;top:1131px">300x600</div>

<div class="banner b160">
  <div class="header-band"></div>
  <div class="brand-name">Clearvale<br>Radon</div>
  <div class="headline">Got Radon?</div>
  <div class="house-art" role="img" aria-label="Cutaway illustration of a house interior with green radon gas rising from the basement"></div>
  <div class="offer-band"><span class="offer-main">Free Estimates</span>Same Day Service<br>Best Price Guarantee</div>
</div>
<div class="size-label" style="left:446px;top:1131px">160x600</div>

<div class="banner b120">
  <div class="header-band"></div>
  <div class="brand-name">Clearvale<br>Radon</div>
  <div class="headline">Got<br>Radon?</div>
  <div class="house-art" role="img" aria-label="Cutaway illustration of a house interior with green radon gas rising from the basement"></div>
  <div class="offer-band"><span class="offer-main">Free<br>Estimates</span><span class="offer-line">Same Day<br>Service</span><span class="offer-line">Best Price<br>Guarantee</span></div>
</div>
<div class="size-label" style="left:681px;top:1131px">120x600</div>

</body>
</html>
```